Talon Burke Construction LLC

I like to have a business card the is unique, very professional and the it will projected the best first impression of me and my company

Target Market(s)

Remodeling, new constitution

Industry/Entity Type

Business

Font styles to use
Script

Requirements
Must have
• My company name email and phone number
Nice to have
• A logo maybe

```html
<!DOCTYPE html>
<html lang="en">
<head>
<meta charset="utf-8">
<title>Talon Burke Construction LLC – Business Card</title>
<link rel="stylesheet" href="https://fonts.googleapis.com/css2?family=Montserrat:wght@300;400;500;700&display=swap">
<style>
  :root {
    --bg: #e3e3e3;
    --card: #f1f1f1;
    --ink: #1e1e1e;
    --dark: #262626;
    --orange: #ef8a17;
    --muted: #2b2b2b;
  }
  * { margin: 0; padding: 0; box-sizing: border-box; }
  html, body { width: 1200px; height: 900px; overflow: hidden; }
  body {
    background: var(--bg);
    font-family: "Montserrat", sans-serif;
    color: var(--ink);
    position: relative;
  }
  .card {
    position: absolute;
    left: 290px;
    width: 620px;
    height: 354px;
    background: var(--card);
    box-shadow: 0 6px 18px rgba(0,0,0,0.12);
    overflow: hidden;
  }
  .card--front { top: 76px; }
  .card--back { top: 470px; }
  .card__art { position: absolute; inset: 0; width: 100%; height: 100%; }

  .brand {
    position: absolute;
    left: 44px;
    top: 140px;
    display: flex;
    align-items: center;
    gap: 14px;
  }
  .brand__mark { width: 30px; height: 30px; background: var(--orange); flex: none; }
  .brand__name {
    font-weight: 700;
    font-size: 25px;
    line-height: 1.15;
    color: var(--ink);
  }

  .contact {
    position: absolute;
    left: 372px;
    top: 78px;
    width: 210px;
  }
  .contact__name {
    font-weight: 500;
    font-size: 19px;
    letter-spacing: 0.5px;
    text-align: right;
    padding-right: 8px;
  }
  .contact__role {
    font-size: 11px;
    color: var(--orange);
    letter-spacing: 1px;
    text-align: right;
    padding-right: 8px;
  }
  .contact__rule { height: 2px; background: var(--ink); margin: 6px 0 12px; }
  .contact__rule--accent { background: var(--orange); width: 130px; margin: 8px 0 8px; }
  .contact__group { display: flex; justify-content: space-between; align-items: center; }
  .contact__lines { font-size: 12.5px; line-height: 1.35; }
  .contact__icon {
    width: 34px; height: 34px;
    background: var(--orange);
    display: flex; align-items: center; justify-content: center;
  }
</style>
</head>
<body>

<section class="card card--front">
  <svg class="card__art" viewBox="0 0 620 354">
    <polygon points="225,0 380,52 358,210 375,354 620,354 620,0" fill="var(--dark)" role="img" aria-label="Dark grey pixel mosaic texture"/>
    <polyline points="225,0 380,52 358,210 375,354" fill="none" stroke="var(--orange)" stroke-width="6"/>
  </svg>
  <div class="brand">
    <div class="brand__mark"></div>
    <div class="brand__name">Talon Burke<br>Construction LLC</div>
  </div>
</section>

<section class="card card--back">
  <svg class="card__art" viewBox="0 0 620 354">
    <polygon points="0,0 228,0 262,78 255,248 420,300 468,354 0,354" fill="var(--dark)" role="img" aria-label="Dark grey pixel mosaic texture"/>
    <polyline points="228,0 262,78 255,248 420,300 468,354" fill="none" stroke="var(--orange)" stroke-width="6"/>
  </svg>
  <div class="contact">
    <div class="contact__name">DANA WHITFIELD</div>
    <div class="contact__role">DIRECTOR</div>
    <div class="contact__rule"></div>
    <div class="contact__group">
      <div class="contact__lines">+012 555 0148<br>+012 555 0149</div>
      <div class="contact__icon">
        <svg width="16" height="16" viewBox="0 0 24 24" aria-label="Phone"><path fill="#fff" d="M6.6 10.8a15.1 15.1 0 0 0 6.6 6.6l2.2-2.2c.3-.3.7-.4 1-.2 1.1.4 2.3.6 3.6.6.6 0 1 .4 1 1V20c0 .6-.4 1-1 1A17 17 0 0 1 3 4c0-.6.4-1 1-1h3.5c.6 0 1 .4 1 1 0 1.3.2 2.5.6 3.6.1.3 0 .7-.2 1l-2.3 2.2z"/></svg>
      </div>
    </div>
    <div class="contact__rule contact__rule--accent"></div>
    <div class="contact__group">
      <div class="contact__lines">dana@talonburke.com<br>talonburke.com</div>
      <div class="contact__icon">
        <svg width="16" height="16" viewBox="0 0 24 24" aria-label="Website"><circle cx="12" cy="12" r="9" fill="none" stroke="#fff" stroke-width="2"/><path d="M3 12h18M12 3c3 3 3 15 0 18M12 3c-3 3-3 15 0 18" fill="none" stroke="#fff" stroke-width="1.6"/></svg>
      </div>
    </div>
  </div>
</section>

</body>
</html>
```